Patriotic Coffee Label

Design a 4"x6" (1200 px x 1800 px) portrait coffee label with a patriotic (USA) feel. The label must include a logo and include a military image. A sample logo and image will be attached. The final files must include .psd (preferred) or .ai templates with layers accessible.

DO NOT place your label on a mock up of a coffee bag! I only need the label design.

If you are the selected winner, you agree to complete the attached Copyright Transfer Agreement.pdf

Document setup:
Artboard: 4 x 6 inches
Color Mode: CMYK
Raster Effects: 300 PPI
Bleed: 0 / none
Output: JPEG, 1200 x 1800px, maximum quality; but .psd or .ai files must be provided with all layers editable.
Design: Edge to edge, background elements fill to artboard boundary

Typefaces: primary is Whitney, for web Whitney Book or Whitney Light for body text, Whitney Semibold, Whitney Bold or Whitney Black for heading. Alternates are Nunito Sans (Google Fonts / Adobe Fonts).
Colors: There are brand colors: old glory blue CMYK 100/87/37/51, old glory red CMYK 8/100/77/1 abd white CMYK 0/0/0/0. Sedondary color is blue CMYK 100/45/0/45 and should represent 20% or less of color usage. Images are exempt, they will be full color, but other elements should follow this guideline. Tertiary colors includ military green, coyote brown, olive, tan sand charcoal, light gray.

Imagery: use provided image, however, the image may be styled in any manner to fit your design vision. Image should be a smart object so that it can be substituted for a similar military image.

Note that other patriotic imagery (US flag) or military symbols can be incorporated as long as they are available in the public domain or you can release copyright.

Design elements that should be included in your design:
1. Logo
2. Name - use "Bramblewood Coffee"
3. Imagery and/or background design
4. Regulatory block - leave bottom 1" clear for regulatory text on readable background.

```html
<!DOCTYPE html>
<html lang="en">
<head>
<meta charset="utf-8">
<title>Bramblewood Coffee Label</title>
<link rel="stylesheet" href="https://fonts.googleapis.com/css2?family=Nunito+Sans:wght@400;800;900&display=swap">
<style>
  :root {
    --page: #e7e7e7;
    --frame-blue: #0f4a7a;
    --old-glory-blue: #1c2a5a;
    --old-glory-red: #c8102e;
    --cream: #f4ecdc;
    --badge-fill: #e4e2db;
    --olive: #4b5524;
    --ink: #3d3d3d;
  }
  * { box-sizing: border-box; margin: 0; padding: 0; }
  html, body {
    width: 1200px; height: 1109px; overflow: hidden;
    background: var(--page);
    font-family: "Nunito Sans", sans-serif;
  }
  .label {
    position: absolute; left: 250px; top: 30px;
    width: 700px; height: 1049px;
    border: 14px solid var(--frame-blue);
    background: var(--cream);
    overflow: hidden;
  }
  .flag-ribbon { position: absolute; left: 0; top: 0; width: 300px; height: 170px; }
  .badge { position: absolute; left: 86px; top: 112px; width: 500px; height: 214px; }
  .brand-name {
    position: absolute; left: 0; right: 0; top: 72px;
    display: flex; justify-content: center; align-items: center; gap: 10px;
  }
  .brand-name__mark { width: 14px; height: 14px; background: var(--old-glory-red); }
  .brand-name__text {
    font-weight: 900; font-size: 30px; line-height: 40px; color: var(--old-glory-blue);
    letter-spacing: 0.5px; text-transform: uppercase;
  }
  .product-title {
    position: absolute; left: 0; right: 0; top: 166px;
    text-align: center; color: var(--olive);
    font-weight: 900; font-size: 46px; line-height: 54px;
    text-transform: uppercase; letter-spacing: 0.5px;
  }
  .hero-photo {
    position: absolute; left: 0; top: 391px; width: 672px; height: 468px;
    background: linear-gradient(180deg, #8d9a5f 0%, #b9ad87 45%, #c9bb94 70%, #8b8470 100%);
  }
  .regulatory {
    position: absolute; left: 28px; top: 890px; width: 468px;
    font-size: 15px; line-height: 22px; color: var(--ink);
    text-align: justify; font-weight: 400;
  }
  .net-quantity {
    position: absolute; left: 530px; top: 934px; width: 116px;
    text-align: center; font-size: 15px; color: var(--ink);
  }
  .net-quantity__value {
    display: inline-block; margin-top: 1px;
    border: 1px solid #9a9a9a; padding: 0 3px; line-height: 20px;
  }
</style>
</head>
<body>
  <main class="label">
    <svg class="flag-ribbon" role="img" aria-label="Waving American flag ribbon across the top-left corner" viewBox="0 0 300 170">
      <defs>
        <linearGradient id="flagTone" x1="0" y1="1" x2="1" y2="0">
          <stop offset="0" stop-color="#223d7a"/>
          <stop offset="0.42" stop-color="#223d7a"/>
          <stop offset="0.5" stop-color="#e43a4a"/>
          <stop offset="1" stop-color="#ef6a74"/>
        </linearGradient>
      </defs>
      <polygon points="0,90 165,0 270,0 0,150" fill="url(#flagTone)"/>
    </svg>

    <svg class="badge" viewBox="0 0 500 214" aria-hidden="true">
      <polygon points="8,107 74,14 426,14 492,107 426,200 74,200"
               fill="var(--badge-fill)" stroke="var(--olive)" stroke-width="4" stroke-linejoin="round"/>
    </svg>

    <div class="brand-name">
      <span class="brand-name__mark"></span>
      <span class="brand-name__text">Liberty Canteen</span>
    </div>

    <h1 class="product-title">Bramblewood<br>Coffee</h1>

    <div class="hero-photo" role="img" aria-label="Soldiers in camouflage taking position beside a tan military utility vehicle in woodland"></div>

    <p class="regulatory">Coffee labeling in the USA is primarily regulated by the Food and Drug Administration (FDA) under the Federal Food, Drug, and Cosmetic Act (FD&amp;C Act) and the Fair Packaging and Labeling Act (FPLA). Coffee is considered a food product, and packaging must contain specific information to be compliant.</p>

    <div class="net-quantity">
      Net Quantity<br>
      <span class="net-quantity__value">8.8 OZ/250GR</span>
    </div>
  </main>
</body>
</html>
```